Wax Heater Box - Re-design

We need a new box design for our wax heater box. We would like our own branding incorporating our logo. The box dimensions are:
20cm wide x 26cm high. Please visit our web site www.lumiskin.com.au and see our logo. It has 5 coloured squares. We could like the box to have some strong,bright squares of colour - very contemporary. It has to appeal mainly to women, but not alienate men as they buy wax pots too. Colour should be as per the logo in lime green, orange, blue, pink and yellow with bits of white/black. We need a photo of the wax heater on the front face. We want something fun, contemporary, bright, bold and colourful.

Main Face:
Lumiskin Australia Logo
Title: Professional Wax Heater
Sub title: 1 litre capacity
Website: www.lumiskn.com.au
hoto of Wax Pot - see file attached

Second Face: TBA

Third Face:Small images of Protective Lid, wax pot insert, locking base/collar and Removable Insert with handle and scraper bar - see images attached.

Text:
Design Features & Functions
- Thermostatically Controlled
- Highest Temperature 95 deg C adjustable
- Indicator Light
- Removable Wax Pot insert with Handle and scraper bar
- Protective Lid
- Locking Base/Drip Collar

Fourth Face: Contact Details:
Lumiskin Australia
Telephone: +61 2 8043 2658
Email: info@lumiskin.com.au
Fax: +61 2 8043 2659
Website: www.lumiskin.com.au

Target Market(s)

Everyone who does waxing at home, beauty therapists, athletes, age approx 20 - 50

Industry/Entity Type

Requirements
Must have
• front face should have a photo of the wax pot - will attach file
Any questions please email me at info@lumiskin.com.au
Should not have
• current box has wax pot on face which we need. this is the current box which needs redesigning.

```html
<!DOCTYPE html>
<html lang="en">
<head>
<meta charset="utf-8">
<title>Lumiskin Professional Wax Heater – Box Faces</title>
<link rel="stylesheet" href="https://fonts.googleapis.com/css2?family=Arimo:ital,wght@0,400;0,700;1,400&display=swap">
<style>
  :root{
    --bg:#e9e9ea;
    --panel:#ffffff;
    --edge:#d4d4d6;
    --ink:#3a3a3c;
    --title:#8e8f93;
    --accent:#e23a2c;
    --lime:#8cc63f;
    --orange:#f39a1e;
    --blue:#2f8fd6;
    --pink:#e0428f;
    --yellow:#f6d21a;
    --purple:#7b3f98;
    --photo-a:#f4f4f6;
    --photo-b:#c9cbd0;
  }
  *{box-sizing:border-box;margin:0;padding:0}
  html,body{width:1200px;height:901px;overflow:hidden}
  body{background:var(--bg);font-family:"Arimo",Arial,sans-serif;color:var(--ink)}
  .dieline{position:absolute;left:90px;top:200px;display:flex;gap:0}
  .face{position:relative;width:340px;height:442px;background:var(--panel);border:1px solid var(--edge);overflow:hidden}
  .lid-tab{position:absolute;left:50%;top:0;transform:translateX(-50%);width:150px;height:70px;border:1px solid var(--edge);border-top:none;border-radius:0 0 12px 12px;display:flex;align-items:center;justify-content:center}
  .brand{display:flex;align-items:center;gap:6px;font-size:17px;font-weight:400;color:var(--ink);letter-spacing:.5px}
  .brand-square{width:10px;height:10px;background:var(--ink)}
  .colour-cluster{position:absolute;border-radius:10px;background:linear-gradient(135deg,var(--purple) 0%,var(--pink) 25%,var(--orange) 50%,var(--lime) 72%,var(--blue) 100%);opacity:.9}
  /* features face */
  .features .colour-cluster{left:60px;top:130px;width:90px;height:80px}
  .features-title{position:absolute;left:26px;top:250px;font-size:11px;font-weight:700}
  .features-list{position:absolute;left:26px;top:268px;width:190px;list-style:none;font-size:10px;line-height:1.5}
  .features-list li::before{content:"- "}
  .part-thumbs{position:absolute;right:26px;top:210px;display:flex;flex-direction:column;gap:10px}
  .part-thumb{width:46px;height:46px;border:1px solid var(--edge);background:linear-gradient(160deg,var(--photo-a),var(--photo-b))}
  /* front face */
  .front .lid-tab{height:90px}
  .product-title{position:absolute;left:0;right:0;top:110px;text-align:center;font-size:38px;line-height:1.05;font-weight:400;color:var(--title)}
  .capacity{position:absolute;left:0;right:0;top:196px;text-align:center;font-size:17px;color:var(--accent)}
  .product-photo{position:absolute;left:70px;top:228px;width:160px;height:170px;border-radius:40px 40px 20px 20px;background:radial-gradient(ellipse at 40% 35%,var(--photo-a),var(--photo-b))}
  .front .colour-cluster{right:22px;top:270px;width:80px;height:110px}
  .front-web{position:absolute;left:0;right:0;bottom:14px;text-align:center;font-size:11px}
  /* contact face */
  .contact .brand{position:absolute;right:30px;top:150px}
  .contact-details{position:absolute;right:30px;top:210px;text-align:right;font-size:11px;line-height:1.6;font-style:italic}
  .contact-details .label{font-style:normal}
</style>
</head>
<body>
<main class="dieline">
  <section class="face features">
    <div class="colour-cluster" role="img" aria-label="Overlapping bright colour squares decoration"></div>
    <h2 class="features-title">Design Features &amp; Functions</h2>
    <ul class="features-list">
      <li>Thermostatically Controlled</li>
      <li>Highest Temperature 95 deg C adjustable</li>
      <li>Indicator Light</li>
      <li>Removable Wax Pot insert with Handle and scraper bar</li>
      <li>Protective Lid</li>
      <li>Locking Base/Drip Collar</li>
    </ul>
    <div class="part-thumbs">
      <div class="part-thumb" role="img" aria-label="Photo of protective lid"></div>
      <div class="part-thumb" role="img" aria-label="Photo of wax pot insert"></div>
      <div class="part-thumb" role="img" aria-label="Photo of locking base and collar"></div>
      <div class="part-thumb" role="img" aria-label="Photo of removable insert with handle and scraper bar"></div>
    </div>
  </section>

  <section class="face front">
    <div class="lid-tab"><span class="brand"><span class="brand-square"></span>Lumiskin</span></div>
    <h1 class="product-title">Professional<br>Wax Heater</h1>
    <p class="capacity">1 Litre capacity</p>
    <div class="product-photo" role="img" aria-label="Photo of the white wax heater pot"></div>
    <div class="colour-cluster" role="img" aria-label="Overlapping bright colour squares decoration"></div>
    <p class="front-web">www.lumiskn.com.au</p>
  </section>

  <section class="face contact">
    <div class="lid-tab"><span class="brand"><span class="brand-square"></span>Lumiskin</span></div>
    <span class="brand">Lumiskin</span>
    <address class="contact-details">
      <span class="label">Contact Details:</span><br>
      Lumiskin Australia<br>
      Telephone: +61 2 8043 2658<br>
      Email: info@lumiskin.com.au<br>
      Fax: +61 2 8043 2659<br>
      Website: www.lumiskin.com.au
    </address>
  </section>
</main>
</body>
</html>
```